Corporate Design für regionale Gebäudetrocknung
Zielgruppe
Ich betreibe seit vielen Jahren ein Unternehmen im Bereich der regionalen Gebäudetrocknung KlimaVeltor.de und möchte auf der Domain KlimaVeltor.de zukünftig ein bundesweites Verzeichniss für Bautrockner, Lüfter und Heizer aufbauen.
Kundengruppe: Verleiher, Vermieter, Trocknungsunternehmen die ihre Geräte und ihre Dienstleistung an privat personen und Gewerbe anbieten möchten.
Nutzergruppe: Bauherren, Renovierer, Eigentumsbesitzer, Mieter, Vermieter, Bauunternehmen, Handwerker, Versicherungen die auf der Suche nach einem Dienstleister für die Trocknung sind.
Wichtig, ich bin zukünftig nicht der Vermieter, sondern nur der Portalbertreiber.
Aufgabenstellung
Ich brauche eine Überarbeitung des bestehenden Logos, eine Gestaltung von Visitenkarten, Geschäftspapier und Favicon in diesem Projekt.
Vorgaben:
- es besteht bereits ein Logo auf dem ich gerne aufbauen möchte (siehe Angehängte Datei)
- es soll bei der Kombination schwarz-gelb bleiben (wenn ihr mich vom Gegenteil überzeug, gerne auch andere Farben ;-))
- die Domain KlimaVeltor.de soll in dem Logo verbleiben, was die Schriftart an geht, freue ich mich auf eure Ideen.
- die darunter liegenden Pictos (Heizen, Trocknen, Lüften) sollen zwingend zu einem Pictogramm zusammengefasst werden.
- mein Ziel ist es das ich das Gesamtlogo (inkl. Domain) nicht immer nutzen muss, sondern auch die Kombination der Pictogramme autark verwenden kann.
- das zu gestaltende Favicon muss nicht zwingend identisch mit den Pictogrammen im Logo sein aber sollte den Schwerpunkt der Plattform nähmlich die Gebäudetrocknung berücksichtigen.
- im Anhang hab ich noch einige Marken eingefügt die mir persönlich gefallen. z.B Brenninger Forst (dort wären die Ziegelsteine aus meiner Sicht das Pictogramm und gleichzeitig des Favicon)

```html
<!DOCTYPE html>
<html lang="de">
<head>
<meta charset="utf-8">
<title>KlimaVeltor.de – Geschäftsausstattung</title>
<link href="https://fonts.googleapis.com/css2?family=Fira+Sans:wght@400;600;700&display=swap" rel="stylesheet">
<style>
  :root {
    --ink: #111111;
    --yellow: #fbef00;
    --paper: #ffffff;
    --stage: #ffffff;
    --mark-line: #9a9a9a;
    --faint: #ececec;
  }
  html, body { margin: 0; padding: 0; }
  body {
    width: 844px; height: 1200px; overflow: hidden;
    background: var(--stage);
    font-family: "Fira Sans", sans-serif; color: var(--ink);
    position: relative;
  }
  .sheet, .card { position: absolute; background: var(--paper); box-shadow: 0 4px 14px rgba(0,0,0,.18); }

  /* Briefbogen */
  .letterhead { left: 150px; top: 104px; width: 540px; height: 764px; }
  .top-bar { position: absolute; left: 0; top: 0; width: 100%; height: 8px; background: var(--ink); }
  .wordmark { position: absolute; display: flex; align-items: center; font-weight: 700; white-space: nowrap; color: var(--ink); letter-spacing: -0.01em; }
  .wordmark .tile { background: var(--yellow); border: 0; display: inline-block; }
  .letterhead .wordmark { right: 22px; top: 54px; font-size: 25px; gap: 6px; }
  .letterhead .wordmark .tile { width: 20px; height: 20px; }
  .address-window { position: absolute; left: 51px; top: 115px; width: 219px; height: 116px; }
  .corner { position: absolute; width: 6px; height: 6px; border-color: var(--mark-line); border-style: solid; border-width: 0; }
  .corner.tl { left: 0; top: 0; border-left-width: 1px; border-top-width: 1px; }
  .corner.tr { right: 0; top: 0; border-right-width: 1px; border-top-width: 1px; }
  .corner.bl { left: 0; bottom: 0; border-left-width: 1px; border-bottom-width: 1px; }
  .corner.br { right: 0; bottom: 0; border-right-width: 1px; border-bottom-width: 1px; }
  .sender { position: absolute; left: 0; right: 0; top: 2px; text-align: center; font-size: 8.4px; line-height: 11px; letter-spacing: 0.04em; }
  .sender strong { font-weight: 600; letter-spacing: 0.02em; }
  .contact-block { position: absolute; left: 398px; top: 117px; font-size: 8.4px; line-height: 11px; font-weight: 600; border-collapse: collapse; }
  .contact-block td { padding: 0; }
  .contact-block td.label { width: 24px; }
  .fold-mark { position: absolute; left: 0; width: 7px; height: 1px; background: var(--mark-line); }
  .fold-mark.upper { top: 269px; }
  .fold-mark.lower { top: 539px; }
  .faint-wordmark { position: absolute; left: 66px; top: 388px; font-size: 42px; font-weight: 700; color: var(--faint); white-space: nowrap; letter-spacing: -0.01em; }
  .footer-band { position: absolute; left: 0; bottom: 0; width: 100%; height: 50px; background: var(--yellow); }
  .footer-col { position: absolute; top: 10px; padding-left: 5px; border-left: 1px solid var(--ink); font-size: 8.3px; line-height: 11px; white-space: nowrap; }
  .footer-col.address { left: 51px; }
  .footer-col.bank { left: 217px; }
  .footer-col.tax { left: 421px; }

  /* Visitenkarten */
  .card { width: 256px; height: 166px; top: 933px; overflow: hidden; }
  .card-front { left: 150px; background: var(--yellow); }
  .card-front .wordmark { left: 32px; top: 66px; font-size: 21px; gap: 5px; }
  .card-front .wordmark .tile { width: 16px; height: 16px; background: var(--ink); }
  .card-back { left: 433px; }
  .card-back .top-bar { height: 6px; }
  .card-back .bottom-bar { position: absolute; left: 0; bottom: 0; width: 100%; height: 8px; background: var(--yellow); }
  .card-back .wordmark { right: 13px; top: 19px; font-size: 15px; gap: 4px; }
  .card-back .wordmark .tile { width: 11px; height: 11px; }
  .holder { position: absolute; left: 12px; top: 102px; font-size: 9px; line-height: 10px; }
  .holder .name { font-weight: 700; letter-spacing: -0.01em; }
  .card-contacts { position: absolute; left: 161px; top: 70px; list-style: none; margin: 0; padding: 0; font-size: 7px; }
  .card-contacts li { display: flex; align-items: flex-start; line-height: 9.5px; margin-bottom: 3.8px; letter-spacing: 0.02em; }
  .card-contacts svg { width: 8px; height: 8px; margin-right: 6px; flex: none; margin-top: 1px; }
</style>
</head>
<body>

<section class="sheet letterhead" aria-label="Briefbogen">
  <div class="top-bar"></div>
  <div class="wordmark"><span class="tile"></span>KlimaVeltor.de</div>

  <div class="address-window">
    <span class="corner tl"></span><span class="corner tr"></span>
    <span class="corner bl"></span><span class="corner br"></span>
    <div class="sender"><strong>KlimaVeltor.de</strong><br>Musterstrasse 123 | 12345 Musterstadt</div>
  </div>

  <table class="contact-block">
    <tr><td class="label">TEL</td><td>0123 / 45 67 89 01</td></tr>
    <tr><td class="label">FAX</td><td>0123 / 45 67 89 01</td></tr>
    <tr><td class="label">MAIL</td><td>info@KlimaVeltor.de</td></tr>
    <tr><td class="label">WEB</td><td>KlimaVeltor.de</td></tr>
  </table>

  <span class="fold-mark upper"></span>
  <span class="fold-mark lower"></span>

  <div class="faint-wordmark" aria-hidden="true">KlimaVeltor.de</div>

  <footer class="footer-band">
    <div class="footer-col address">Musterstrasse 123<br>12345 Musterstadt<br>Geschäftsführer: Max Muster</div>
    <div class="footer-col bank">Bankverbindung<br>BIC:&nbsp;&nbsp;&nbsp; ABCDEFGHXXX<br>IBAN: DE 12 3333 4444 5555 6666 77</div>
    <div class="footer-col tax">Finanzamt Musterstadt<br>USt-IdNr.:<br>DE123456789</div>
  </footer>
</section>

<section class="card card-front" aria-label="Visitenkarte Vorderseite">
  <div class="wordmark"><span class="tile"></span>KlimaVeltor.de</div>
</section>

<section class="card card-back" aria-label="Visitenkarte Rückseite">
  <div class="top-bar"></div>
  <div class="wordmark"><span class="tile"></span>KlimaVeltor.de</div>
  <div class="holder"><div class="name">MAX MUSTER</div>Geschäftsführer</div>
  <ul class="card-contacts">
    <li><svg viewBox="0 0 10 10"><path d="M5 9.5 C3 6.5 1.8 5 1.8 3.6 A3.2 3.2 0 0 1 8.2 3.6 C8.2 5 7 6.5 5 9.5Z" fill="none" stroke="#111" stroke-width="1.2"/><circle cx="5" cy="3.6" r="1" fill="#111"/></svg><span>Musterstrasse 123<br>12345 Musterstadt</span></li>
    <li><svg viewBox="0 0 10 10"><path d="M2.5 1 L4 3.5 L3 4.5 Q4.2 6.8 5.8 7.2 L6.8 6.2 L9 7.6 L8 9.3 Q3.5 9 1 2.4Z" fill="#111"/></svg><span>0123 / 45 67 89 01</span></li>
    <li><svg viewBox="0 0 10 10"><rect x="2.5" y="1" width="5" height="3" fill="none" stroke="#111"/><rect x="0.8" y="4.5" width="8.4" height="4.5" fill="#111"/></svg><span>0123 / 45 67 89 01</span></li>
    <li><svg viewBox="0 0 10 10"><rect x="3" y="0.8" width="4.4" height="8.4" rx="0.8" fill="#111" transform="rotate(-20 5 5)"/></svg><span>0123 / 45 67 89 01</span></li>
    <li><svg viewBox="0 0 10 10"><rect x="0.6" y="2" width="8.8" height="6" fill="#111"/><path d="M0.6 2 L5 5.6 L9.4 2" fill="none" stroke="#fff" stroke-width="0.9"/></svg><span>info@nordbrise-web.de</span></li>
    <li><svg viewBox="0 0 10 10"><circle cx="5" cy="5" r="4" fill="none" stroke="#111"/><ellipse cx="5" cy="5" rx="1.8" ry="4" fill="none" stroke="#111" stroke-width="0.8"/><path d="M1 5 H9 M1.8 3 H8.2 M1.8 7 H8.2" stroke="#111" stroke-width="0.7"/></svg><span>nordbrise-web.de</span></li>
  </ul>
  <div class="bottom-bar"></div>
</section>

</body>
</html>
```